VELVET ANVIL - BOOK COVER

I have written a book called VELVET ANVIL - HOW TO CLIMB PAST EVERY LIMIT AT FULL THROTTLE. I need a front cover design for the book. The book cover needs to be intriguing for someone to pick it up and read the first couple of pages. I want people to think about ACHIEVING SUCCESS when they read this book.
PLEASE LOOK AT THE ATTACHMENT. THANKS!

Target Market(s)

males, entrepreneurs, small business owners, salespeople, corporate executives

Industry/Entity Type

Business

Logo Text

VELVET ANVIL

Logo styles of interest
Emblem Logo
Abstract Logo
Font styles to use
Serif
Sans Serif

Colors
ec1f27
000000
959595
ffffff

Requirements
Must have
• It has to have a "hurricane" feel to it with hurricane colors.
Nice to have
• I open to your ideas
Should not have
• no other colors except red, black, gray, white.

```html
<!DOCTYPE html>
<html lang="en">
<head>
<meta charset="utf-8">
<title>Velvet Anvil – Book Cover</title>
<link rel="stylesheet" href="https://fonts.googleapis.com/css2?family=Bebas+Neue&family=Montserrat:wght@600&display=swap">
<style>
  :root {
    --red: #ec1f27;
    --red-deep: #6e1418;
    --black: #000000;
    --charcoal: #1c1c1c;
    --graphite: #383838;
    --gray: #959595;
    --white: #ffffff;
    --backdrop: #ece9e3;
  }
  html, body {
    margin: 0;
    width: 1200px;
    height: 1039px;
    overflow: hidden;
    background: var(--backdrop);
  }
  .cover {
    position: absolute;
    left: 260px;
    top: 50px;
    width: 680px;
    height: 940px;
    overflow: hidden;
    background: radial-gradient(ellipse at 55% 40%, var(--graphite) 0%, var(--charcoal) 55%, #0d0d0d 100%);
    box-shadow: 0 10px 30px rgba(0,0,0,0.25);
  }
  .corner-arcs {
    position: absolute;
    left: 0;
    top: 0;
    width: 680px;
    height: 940px;
  }
  .title {
    position: absolute;
    left: 0;
    right: 0;
    top: 152px;
    margin: 0;
    text-align: center;
    font-family: "Bebas Neue", "Oswald", sans-serif;
    font-weight: 400;
    font-size: 122px;
    line-height: 0.94;
    letter-spacing: 3px;
    color: var(--white);
  }
  .title span { display: block; }
  .storm-art {
    position: absolute;
    left: 277px;
    top: 396px;
    width: 126px;
    height: 156px;
    border-radius: 6px;
    background: linear-gradient(180deg, rgba(149,149,149,0.55) 0%, rgba(149,149,149,0.3) 100%);
  }
  .subtitle {
    position: absolute;
    left: 0;
    right: 0;
    top: 588px;
    margin: 0;
    text-align: center;
    font-family: "Bebas Neue", "Oswald", sans-serif;
    font-weight: 400;
    font-size: 62px;
    line-height: 70px;
    letter-spacing: 0.5px;
  }
  .subtitle .accent { display: block; color: var(--red); }
  .subtitle .highlight {
    display: flex;
    align-items: center;
    justify-content: center;
    gap: 22px;
    color: var(--white);
  }
  .subtitle .highlight::before,
  .subtitle .highlight::after {
    content: "";
    width: 58px;
    height: 5px;
    background: var(--white);
  }
  .author-band {
    position: absolute;
    left: 0;
    right: 0;
    top: 832px;
    height: 71px;
    background: var(--red);
    display: flex;
    align-items: center;
    justify-content: center;
    font-family: "Montserrat", "Helvetica Neue", sans-serif;
    font-weight: 600;
    font-size: 36px;
    letter-spacing: 2px;
    color: var(--white);
  }
</style>
</head>
<body>
  <main class="cover">
    <svg class="corner-arcs" viewBox="0 0 680 940" aria-hidden="true">
      <g fill="none" stroke="var(--red-deep)">
        <path d="M0 260 A 300 300 0 0 1 120 0" stroke-width="16"/>
        <path d="M0 200 A 250 250 0 0 1 80 0" stroke-width="14"/>
        <path d="M0 140 A 200 200 0 0 1 42 0" stroke-width="12"/>
        <path d="M680 640 A 300 300 0 0 0 520 940" stroke-width="16"/>
        <path d="M680 710 A 250 250 0 0 0 580 940" stroke-width="14"/>
        <path d="M680 780 A 200 200 0 0 0 630 940" stroke-width="12"/>
      </g>
    </svg>

    <h1 class="title"><span>Velvet</span><span>Anvil</span></h1>

    <div class="storm-art" role="img" aria-label="Gray storm illustration"></div>

    <p class="subtitle">
      <span class="accent">How to climb past</span>
      <span class="highlight">Every limit</span>
      <span class="accent">At full throttle</span>
    </p>

    <div class="author-band">CAL DRENNAN</div>
  </main>
</body>
</html>
```